Copperline Ridge Footraces

We need a website (wordpress) design for a new website that we will be launching. This is for a new trail racing series in Canada.
We recently had a logo designed so want to incorporate the colours of the logo on the website design. Especially the dark blue, green and orange.
Websites that we like for comparison of trail running race themes are:
https://www.brambleroutefest.com/
https://www.stridecolmcircuit.com/
http://www.fernpathcircuit.ca/
https://www.silvanloopcircuit.com/
http://www.marbrookrunlineup.com/

Target Market(s)

Outdoor trail runners

Coding

Coded - Design and coding required

Number of Pages Required

4 page

Font styles to use
Sans Serif

Colors
0255a3
33b8a4
f37122

Requirements
Must have
• There will be a main page with eye catching design noting what we do. Page 2 and 3 will be for each race in the series. Page 1 will be a specific race, and page 2 with be for another race. page 3 and 4 will be for future races that we add so that each race has their own page.
• Our races all take place in the mountains, so using graphics including mountains, rivers, trees is all a requirement for us.
• Our logo is attached, we want to use the colours of the logo in the website design.
Nice to have
• Outdoor theme is a nice to have. We like wood and earth tone colours, and pictures/graphics of runners and mountains and trees.
• There are 4 people involved in our organization. We'd like a photo and brief blurb of each of us, similar to how this website did their layout: https://www.brambleroutefest.com/

```html
<!DOCTYPE html>
<html lang="en">
<head>
<meta charset="utf-8">
<title>Copperline Ridge Footraces</title>
<link rel="stylesheet" href="https://fonts.googleapis.com/css2?family=Montserrat:wght@400;500;600;700;800&display=swap">
<style>
:root{
  --blue:#0255a3;
  --teal:#33b8a4;
  --orange:#f37122;
  --green:#7cb342;
  --ink:#1d1d1d;
  --muted:#555;
  --footer:#232323;
  --footer-bottom:#161616;
  --white:#fff;
}
*{margin:0;padding:0;box-sizing:border-box}
html,body{width:1200px;height:2804px;overflow:hidden;background:var(--white)}
body{position:relative;font-family:"Montserrat",Arial,sans-serif;color:var(--ink)}
.abs{position:absolute}

/* hero */
.hero{left:0;top:0;width:1200px;height:680px}
.hero-photo{left:0;top:0;width:1200px;height:680px;
  background:
    radial-gradient(ellipse 420px 520px at 760px 300px,rgba(40,40,44,.45),rgba(40,40,44,0) 70%),
    radial-gradient(ellipse 700px 300px at 300px 80px,rgba(245,243,238,.85),rgba(245,243,238,0) 75%),
    radial-gradient(ellipse 600px 160px at 500px 640px,rgba(86,120,52,.55),rgba(86,120,52,0) 70%),
    linear-gradient(180deg,#e6e3dc 0%,#c9bba5 28%,#a18866 52%,#76603f 74%,#4f4030 100%)}
.torn-edge{left:0;top:620px;width:1200px;height:60px}
.brand{left:164px;top:96px;width:170px;display:flex;align-items:flex-start;gap:10px}
.brand-mark{width:18px;height:18px;background:var(--blue);flex:none;margin-top:4px}
.brand-name{font-weight:800;font-size:22px;line-height:1.05;color:var(--blue);text-transform:uppercase}
.main-nav{left:411px;top:112px;width:640px;display:flex;justify-content:space-between}
.main-nav a{font-size:12px;font-weight:600;color:var(--ink);text-decoration:none;letter-spacing:.3px}
.hero-box{left:161px;top:415px;width:480px;height:152px;border:3px solid var(--white);padding:26px 30px}
.hero-title{color:var(--white);font-size:23px;font-weight:600;line-height:1.3;text-transform:uppercase}
.hero-link{display:inline-block;margin-top:16px;color:var(--white);font-size:14px;font-weight:700;text-decoration:underline;text-transform:uppercase}

/* section heading */
.section-title{left:0;width:1200px;text-align:center;font-size:32px;font-weight:700;text-transform:uppercase;letter-spacing:.3px}
.section-rule{left:161px;width:878px;height:2px;background:#9fb6d6}
.section-rule::after{content:"";position:absolute;left:409px;top:-2px;width:60px;height:6px;background:var(--blue)}

/* race cards */
.race{width:187px}
.race-logo{width:187px;height:149px;border:3px solid;display:flex;align-items:center;justify-content:center}
.race-logo span{font-size:18px;font-weight:700;text-transform:uppercase;text-align:center;line-height:1.2}
.race-btn{display:block;margin-top:8px;width:187px;height:34px;line-height:34px;text-align:center;color:var(--white);font-size:12px;font-weight:600;text-transform:uppercase}
.race-meta{margin-top:18px;display:grid;grid-template-columns:62px 1fr;row-gap:6px;font-size:9px;font-weight:500;color:var(--ink)}
.race-meta dt{font-weight:700;white-space:nowrap;line-height:14px}
.race-meta dd{line-height:14px;text-align:right;white-space:nowrap}
.race-meta dd.loc{white-space:normal;line-height:13px}
.c-orange{border-color:var(--orange);color:var(--orange)} .b-orange{background:var(--orange)}
.c-teal{border-color:var(--teal);color:var(--teal)} .b-teal{background:var(--teal)}
.c-green{border-color:var(--green);color:var(--green)} .b-green{background:var(--green)}
.c-black{border-color:#111;color:#111} .b-black{background:#111}

/* results band */
.results-band{left:0;top:1219px;width:1200px;height:381px}
.results-photo{left:0;top:0;width:1200px;height:381px;
  background:
    radial-gradient(ellipse 260px 340px at 930px 160px,rgba(150,150,145,.75),rgba(150,150,145,0) 70%),
    radial-gradient(ellipse 500px 90px at 300px 230px,rgba(70,80,100,.55),rgba(70,80,100,0) 70%),
    radial-gradient(ellipse 160px 260px at 80px 150px,rgba(120,80,50,.7),rgba(120,80,50,0) 70%),
    linear-gradient(180deg,#0b4fa8 0%,#2f73c0 28%,#6f9fd4 44%,#5b7a3e 58%,#4f6e30 78%,#3c5424 100%)}
.results-shapes{left:0;top:0;width:1200px;height:381px}
.results-box{left:374px;top:89px;width:450px;height:198px;background:var(--orange);border:3px solid var(--white);text-align:center;padding-top:22px}
.results-title{color:var(--white);font-size:26px;font-weight:700;text-transform:uppercase}
.results-races{display:flex;justify-content:center;gap:18px;margin-top:22px}
.results-races span{width:62px;height:62px;border-radius:50%;background:var(--white);color:var(--orange);font-size:9px;font-weight:700;text-transform:uppercase;display:flex;align-items:center;justify-content:center;text-align:center;line-height:1.15;padding:4px}
.results-link{display:inline-block;margin-top:22px;color:var(--white);font-size:10px;font-weight:700;text-decoration:underline;text-transform:uppercase}

/* team */
.member{width:198px}
.member-photo{position:relative;width:198px;height:205px;background:radial-gradient(ellipse 70px 110px at 99px 130px,#8a8a8c,#b8b8b8 60%,#d8d8d8 100%);border:2px solid #eee;overflow:hidden}
.member-photo svg{position:absolute;left:0;top:0}
.member-name{margin-top:28px;font-size:13px;font-weight:700;text-transform:uppercase}
.member-role{margin-top:14px;font-size:12px;color:var(--muted)}
.member-btn{display:inline-block;margin-top:20px;width:107px;height:34px;line-height:34px;text-align:center;background:var(--orange);color:var(--white);font-size:10px;font-weight:700;text-transform:uppercase}

/* about */
.about{left:0;top:2235px;width:718px;height:303px;background:var(--teal);padding:56px 0 0 161px}
.about-title{color:var(--white);font-size:24px;font-weight:600;text-transform:uppercase;white-space:nowrap}
.about-rule{width:505px;height:2px;background:var(--white);margin-top:14px}
.about-text{margin-top:22px;width:510px;color:var(--white);font-size:11.5px;line-height:1.65}
.about-btn{display:inline-block;margin-top:22px;width:149px;height:42px;line-height:42px;text-align:center;background:var(--white);color:var(--ink);font-size:14px;font-weight:600;text-transform:uppercase}
.about-photo{left:718px;top:2235px;width:482px;height:303px;
  background:
    radial-gradient(ellipse 70px 140px at 290px 150px,rgba(40,40,60,.6),rgba(40,40,60,0) 75%),
    radial-gradient(ellipse 220px 60px at 90px 200px,rgba(80,78,70,.8),rgba(80,78,70,0) 75%),
    linear-gradient(180deg,#e4e5e2 0%,#c4c7c2 35%,#8f958c 62%,#6b6f66 82%,#b7b4ae 100%)}

/* footer */
.footer{left:0;top:2538px;width:1200px;height:209px;background:var(--footer)}
.footer-brand{left:164px;top:70px;width:150px;display:flex;gap:10px;align-items:flex-start}
.footer-brand .brand-name{color:var(--white);font-size:20px}
.footer-brand .brand-mark{background:var(--orange)}
.footer-links{left:411px;top:88px;display:grid;grid-template-columns:135px 146px 140px;row-gap:22px}
.footer-links a{color:var(--white);font-size:10px;font-weight:600;text-decoration:none;text-transform:uppercase;display:flex;align-items:center;gap:8px}
.footer-links a::before{content:"";width:7px;height:7px;border:1.5px solid var(--white)}
.signin{left:824px;top:50px;width:300px;color:var(--white)}
.signin h3{font-size:19px;font-weight:600}
.signin p{margin-top:12px;font-size:10px;line-height:1.4;width:200px}
.signin a{display:inline-block;margin-top:12px;width:103px;height:40px;line-height:40px;text-align:center;background:var(--teal);color:var(--white);font-size:14px;font-weight:600;text-transform:uppercase;text-decoration:none}
.footer-bottom{left:0;top:2747px;width:1200px;height:57px;background:var(--footer-bottom)}
.copyright{left:161px;top:22px;color:#ddd;font-size:10px}
.social{left:955px;top:16px;display:flex;gap:8px}
.social span{width:24px;height:24px;border:1.5px solid #ddd;border-radius:50%}
</style>
</head>
<body>

<header class="hero abs">
  <div class="hero-photo abs" role="img" aria-label="Trail runners on a misty forest path among trees, close view of a runner's legs on grassy earth"></div>
  <svg class="torn-edge abs" viewBox="0 0 1200 60" preserveAspectRatio="none" aria-hidden="true">
    <path d="M0 22 L20 28 L40 24 L60 32 L80 18 L105 30 L130 26 L150 34 L170 24 L195 31 L220 28 L245 36 L270 20 L295 29 L320 32 L345 25 L370 30 L395 36 L420 28 L445 33 L470 22 L495 30 L520 34 L545 27 L570 31 L595 38 L620 29 L645 33 L670 24 L695 30 L720 34 L745 26 L770 22 L795 31 L820 36 L845 28 L870 30 L895 35 L920 27 L945 31 L970 24 L995 29 L1020 32 L1045 27 L1070 30 L1095 35 L1120 28 L1140 31 L1160 24 L1180 29 L1200 26 L1200 60 L0 60 Z" fill="#fff"/>
  </svg>
  <div class="brand abs"><span class="brand-mark"></span><span class="brand-name">Copperline Ridge Footraces</span></div>
  <nav class="main-nav abs">
    <a href="#">HOME</a><a href="#">RACES</a><a href="#">PHOTOS</a><a href="#">RESULTS</a><a href="#">EXPO</a><a href="#">INITIATIVES</a><a href="#">BADGES</a><a href="#">BLOG</a>
  </nav>
  <div class="hero-box abs">
    <h1 class="hero-title">Welcome to the Copperline Ridge Footraces</h1>
    <a class="hero-link" href="#">Trail Race</a>
  </div>
</header>

<h2 class="section-title abs" style="top:765px">Ontario Ultra &amp; Trail Race Series</h2>
<div class="section-rule abs" style="top:825px"></div>

<article class="race abs" style="left:168px;top:871px">
  <div class="race-logo c-orange"><span>Trailhead Dash</span></div>
  <a class="race-btn b-orange">Register Here</a>
  <dl class="race-meta"><dt>DATE :</dt><dd>January 5, 2019</dd><dt>TIME :</dt><dd>9am (1h &amp; 6h) 10:30am (3h)</dd><dt>LOCATION :</dt><dd class="loc">Northgate Athletic Centre - Ashford</dd></dl>
</article>
<article class="race abs" style="left:392px;top:871px">
  <div class="race-logo c-teal"><span>Ridge Relay</span></div>
  <a class="race-btn b-teal">Register Here</a>
  <dl class="race-meta"><dt>DATE :</dt><dd>January 5, 2019</dd><dt>TIME :</dt><dd>9am (1h &amp; 6h) 10:30am (3h)</dd><dt>LOCATION :</dt><dd class="loc">Northgate Athletic Centre - Ashford</dd></dl>
</article>
<article class="race abs" style="left:617px;top:871px">
  <div class="race-logo c-green"><span>Cedar Loop</span></div>
  <a class="race-btn b-green">Register Here</a>
  <dl class="race-meta"><dt>DATE :</dt><dd>January 5, 2019</dd><dt>TIME :</dt><dd>9am (1h &amp; 6h) 10:30am (3h)</dd><dt>LOCATION :</dt><dd class="loc">Northgate Athletic Centre - Ashford</dd></dl>
</article>
<article class="race abs" style="left:843px;top:871px">
  <div class="race-logo c-black"><span>Granite Run</span></div>
  <a class="race-btn b-black">Register Here</a>
  <dl class="race-meta"><dt>DATE :</dt><dd>January 5, 2019</dd><dt>TIME :</dt><dd>9am (1h &amp; 6h) 10:30am (3h)</dd><dt>LOCATION :</dt><dd class="loc">Northgate Athletic Centre - Ashford</dd></dl>
</article>

<section class="results-band abs">
  <div class="results-photo abs" role="img" aria-label="Green mountain ridges and forested slopes under a blue sky, with a trail runner on the right"></div>
  <svg class="results-shapes abs" viewBox="0 0 1200 381" aria-hidden="true">
    <polygon points="0,150 270,381 0,381" fill="#33b8a4"/>
    <polygon points="1200,110 930,381 1200,381" fill="#33b8a4"/>
  </svg>
  <div class="results-box abs">
    <h2 class="results-title">Results</h2>
    <div class="results-races"><span>Trailhead Dash</span><span>Cedar Loop</span><span>Granite Run</span><span>Ridge Relay</span></div>
    <a class="results-link" href="#">Read More</a>
  </div>
</section>

<h2 class="section-title abs" style="top:1682px">Our Team</h2>
<div class="section-rule abs" style="top:1739px"></div>

<article class="member abs" style="left:163px;top:1828px">
  <div class="member-photo" role="img" aria-label="Portrait of race director Owen Marchetti">
    <svg width="198" height="205" viewBox="0 0 198 205" aria-hidden="true"><polygon points="0,0 36,0 0,36" fill="#0255a3"/><polygon points="162,0 198,0 198,36" fill="#33b8a4"/><polygon points="0,170 0,205 36,205" fill="#33b8a4"/><polygon points="198,170 198,205 162,205" fill="#0255a3"/></svg>
  </div>
  <h3 class="member-name">Owen Marchetti</h3><p class="member-role">Race Director</p><a class="member-btn">Learn More</a>
</article>
<article class="member abs" style="left:387px;top:1828px">
  <div class="member-photo" role="img" aria-label="Portrait of race coordinator Lena Vasquez">
    <svg width="198" height="205" viewBox="0 0 198 205" aria-hidden="true"><polygon points="0,0 36,0 0,36" fill="#0255a3"/><polygon points="162,0 198,0 198,36" fill="#33b8a4"/><polygon points="0,170 0,205 36,205" fill="#33b8a4"/><polygon points="198,170 198,205 162,205" fill="#0255a3"/></svg>
  </div>
  <h3 class="member-name">Lena Vasquez</h3><p class="member-role">Race Coordinator</p><a class="member-btn">Learn More</a>
</article>
<article class="member abs" style="left:611px;top:1828px">
  <div class="member-photo" role="img" aria-label="Portrait of race director Owen Marchetti">
    <svg width="198" height="205" viewBox="0 0 198 205" aria-hidden="true"><polygon points="0,0 36,0 0,36" fill="#0255a3"/><polygon points="162,0 198,0 198,36" fill="#33b8a4"/><polygon points="0,170 0,205 36,205" fill="#33b8a4"/><polygon points="198,170 198,205 162,205" fill="#0255a3"/></svg>
  </div>
  <h3 class="member-name">Owen Marchetti</h3><p class="member-role">Race Director</p><a class="member-btn">Learn More</a>
</article>
<article class="member abs" style="left:835px;top:1828px">
  <div class="member-photo" role="img" aria-label="Portrait of race coordinator Lena Vasquez">
    <svg width="198" height="205" viewBox="0 0 198 205" aria-hidden="true"><polygon points="0,0 36,0 0,36" fill="#0255a3"/><polygon points="162,0 198,0 198,36" fill="#33b8a4"/><polygon points="0,170 0,205 36,205" fill="#33b8a4"/><polygon points="198,170 198,205 162,205" fill="#0255a3"/></svg>
  </div>
  <h3 class="member-name">Lena Vasquez</h3><p class="member-role">Race Coordinator</p><a class="member-btn">Learn More</a>
</article>

<section class="about abs">
  <h2 class="about-title">About Copperline Ridge Footraces</h2>
  <div class="about-rule"></div>
  <p class="about-text">Summit Path Racing is run by nature and adventure enthusiasts who aim to provide opportunities in which to engage the running community, explore new terrain, and support those in need.</p>
  <a class="about-btn">Learn More</a>
</section>
<div class="about-photo abs" role="img" aria-label="Trail runner crossing rocky mountain ground above a misty river valley with trees"></div>

<footer class="footer abs">
  <div class="footer-brand abs"><span class="brand-mark"></span><span class="brand-name">Copperline Ridge Footraces</span></div>
  <nav class="footer-links abs">
    <a href="#">Home</a><a href="#">How to Play</a><a href="#">Newsletter</a>
    <a href="#">Club News</a><a href="#">Events</a><a href="#">Contact Us</a>
  </nav>
  <div class="signin abs">
    <h3>Member and Club sign in</h3>
    <p>Member and Club sign in Member and Club sign in</p>
    <a href="#">Sign In</a>
  </div>
</footer>
<div class="footer-bottom abs">
  <p class="copyright abs">© Copyright Copperline Ridge Footraces 2018. All Rights Reserved.</p>
  <div class="social abs"><span></span><span></span><span></span></div>
</div>

</body>
</html>
```